Tolmek Ltd

I have been recommended by my web builder to get a fully designed website from two different companies such as yourselves. I have 5 products initially and need a site with world wide appeal.

Target Market(s)

Care Home and Nail Bar Industry

Industry/Entity Type

Builder

Number of Pages Required

5+ page

Font styles to use
Sans Serif

Colors

Designer to choose colors to be used in the design.

Requirements
Must have
• Great Innovative Home Page
Nice to have
• I would like the background moving as in clouds rushing past. Similar to the way car lights are speeded up in night time ads. I have kel-vex quality shots of various cloud formations that I can send
Should not have
• Usual boring design

```html
<!DOCTYPE html>
<html lang="en">
<head>
<meta charset="utf-8">
<title>Tolmek Ltd – Care Home and Nail Bar Industry</title>
<link rel="stylesheet" href="https://fonts.googleapis.com/css2?family=Open+Sans:ital,wght@0,400;0,600;0,700;1,400&display=swap">
<style>
:root{
  --blue:#1a7fd6;
  --blue-deep:#0f5fb3;
  --navy:#1d3f7a;
  --teal:#1a9a8f;
  --orange:#f7890f;
  --orange-btn:#f59a12;
  --yellow:#f6c21b;
  --ink:#2b2b2b;
  --muted:#6f6f6f;
  --line:#d9d9d9;
  --topbar:#f1f1f1;
  --panel:#ececec;
  --white:#ffffff;
}
*{margin:0;padding:0;box-sizing:border-box}
html,body{width:1200px;height:3523px;overflow:hidden}
body{position:relative;font-family:"Open Sans",Arial,sans-serif;color:var(--ink);background:var(--white)}
.abs{position:absolute}
a{color:inherit;text-decoration:none}

/* top bar */
.topbar{left:0;top:0;width:1200px;height:42px;background:var(--topbar)}
.topbar-phone{left:130px;top:11px;font-size:15px;display:flex;align-items:center;gap:6px}
.topbar-links{right:132px;top:11px;font-size:14px;display:flex;gap:8px;align-items:center}
.topbar-links span.sep{color:#999}

/* header */
.header{left:0;top:42px;width:1200px;height:115px;background:var(--white)}
.brand{left:116px;top:78px;display:flex;align-items:center;gap:12px}
.brand-dot{width:34px;height:34px;border-radius:50%;background:var(--blue)}
.brand-name{font-size:40px;font-weight:700;color:var(--navy);letter-spacing:1px}
.nav{left:470px;top:96px;display:flex;gap:34px;font-size:17px;font-weight:600;color:#333}
.nav .active{color:var(--teal)}

/* hero */
.hero{left:0;top:157px;width:1200px;height:552px;
  background:linear-gradient(180deg,#2c6fd1 0%,#4f8fe0 35%,#a9c8ee 62%,#dfe8f3 80%,#4f6e92 92%,#2f4868 100%)}
.play{left:545px;top:312px;width:94px;height:94px;border:4px solid var(--white);border-radius:50%}
.hero-title{left:0;top:410px;width:1200px;text-align:center;color:var(--white);font-size:41px;font-weight:600}
.hero-sub{left:0;top:466px;width:1200px;text-align:center;color:var(--white);font-size:28px;font-weight:600}

/* welcome */
.welcome-title{left:133px;top:770px;font-size:36px;font-weight:400;color:#222}
.welcome-text{left:136px;top:834px;width:500px;font-size:14.5px;line-height:23px;color:var(--muted)}
.welcome-text p{margin-bottom:16px}
.btn-more{left:136px;top:1003px;width:148px;height:40px;background:var(--orange-btn);color:var(--white);
  font-size:13px;font-weight:700;display:flex;align-items:center;justify-content:center}
.welcome-photo{left:668px;top:730px;width:308px;height:308px;border-radius:50%;border:5px solid #eee;
  background:radial-gradient(circle at 50% 55%,#f1c8b2 0%,#e6a58e 45%,#f7eeee 80%)}

/* why choose */
.why{left:0;top:1115px;width:1200px;height:489px;background:var(--panel)}
.why-photo{left:0;top:1115px;width:563px;height:489px;
  background:linear-gradient(100deg,#f1f1f3 0%,#f3d7cc 45%,#ece9ea 100%)}
.why-title{left:602px;top:1183px;font-size:29px;line-height:38px;color:var(--blue-deep)}
.why-text{left:602px;top:1272px;width:480px;font-size:13.5px;line-height:22px;color:var(--muted)}
.feature{width:250px;padding-left:14px;border-left:1px solid #aaa}
.feature h4{font-size:17px;font-weight:400;color:#333}
.feature p{font-size:12px;color:var(--muted);margin-top:4px}

/* products */
.products{left:0;top:1604px;width:1200px;height:502px;
  background:linear-gradient(180deg,#f7f7f7 0%,#fafafa 60%,#f3ebe9 100%)}
.section-title{font-size:30px;color:#222}
.products-title{left:0;top:1636px;width:1200px;text-align:center}
.product-card{top:1702px;width:228px;height:317px;background:var(--white);border:1px solid var(--line)}
.product-img{position:absolute;left:39px;top:22px;width:150px;height:160px;background:linear-gradient(180deg,#f4f4f4,#e3e3e3)}
.product-name{position:absolute;top:212px;width:100%;text-align:center;font-size:18px;font-weight:600}
.product-desc{position:absolute;top:240px;width:100%;text-align:center;font-size:11.5px;color:var(--muted)}
.product-bar{position:absolute;left:0;bottom:0;width:100%;height:36px;display:flex}
.price{width:50%;background:var(--yellow);color:var(--white);font-size:17px;display:flex;align-items:center;justify-content:center}
.buy{width:50%;background:var(--blue);color:var(--white);font-size:13px;display:flex;align-items:center;justify-content:center}

/* testimonials */
.testimonials{left:0;top:2106px;width:1200px;height:460px;background:var(--orange)}
.test-title{left:0;top:2146px;width:1200px;text-align:center;color:var(--white);font-size:30px}
.quote-card{top:2219px;width:374px;height:180px;border:2px solid rgba(255,255,255,.55);border-radius:22px}
.quote-text{position:absolute;left:62px;top:18px;width:290px;color:var(--white);font-size:13px;font-style:italic;line-height:20px;font-weight:600}
.quote-author{position:absolute;left:62px;top:130px;color:var(--white);font-size:14px}
.avatar{top:2247px;width:92px;height:92px;border-radius:50%;border:4px solid var(--white);
  background:linear-gradient(160deg,#d9c2b2,#b8998a)}

/* blog */
.blog-title{left:113px;top:2583px}
.blog-card{top:2646px;width:306px;height:328px;background:var(--white);border:1px solid #cfcfcf}
.blog-img{position:absolute;left:0;top:0;width:100%;height:166px;background:linear-gradient(135deg,#f6e2d8,#e8c6b6 60%,#f4ede9)}
.blog-date{position:absolute;left:14px;top:187px;width:66px;height:66px;border-radius:50%;border:2px solid var(--blue-deep);
  display:flex;flex-direction:column;align-items:center;justify-content:center;color:var(--navy)}
.blog-date b{font-size:20px;line-height:22px;font-weight:600}
.blog-date span{font-size:10px;font-weight:600}
.blog-head{position:absolute;left:98px;top:186px;font-size:16px;font-weight:600;color:var(--blue-deep)}
.blog-text{position:absolute;left:98px;top:212px;width:190px;font-size:12px;line-height:17px;color:var(--muted)}
.blog-more{position:absolute;left:98px;top:290px;font-size:11.5px;font-weight:700;color:#333}

/* footer */
.footer-wave{left:0;top:3010px;width:1200px;height:513px}
.footer-col{top:3124px;color:var(--white)}
.footer-col h5{font-size:17px;font-weight:400;letter-spacing:.5px;margin-bottom:10px}
.footer-col li{list-style:none;font-size:14px;line-height:28px}
.social{top:3285px;left:155px;display:flex;gap:14px}
.social i{display:block;width:30px;height:30px;border-radius:50%;border:2px solid var(--white);background:rgba(255,255,255,.15)}
.contact-item{display:flex;gap:10px;font-size:14px;line-height:22px;margin-bottom:12px}
.contact-item svg{flex:none;margin-top:3px}
.payments{left:838px;top:3316px;display:flex;gap:8px}
.payments i{display:block;width:42px;height:26px;background:var(--white);border-radius:3px}
.footer-rule{left:130px;top:3438px;width:940px;height:1px;background:rgba(255,255,255,.3)}
.copyright{left:0;top:3462px;width:1200px;text-align:center;color:var(--white);font-size:12px}
</style>
</head>
<body>

<!-- top bar -->
<div class="abs topbar"></div>
<div class="abs topbar-phone">
  <svg width="16" height="16" viewBox="0 0 24 24" aria-hidden="true"><path fill="#1a7fd6" d="M6.6 10.8a15.1 15.1 0 0 0 6.6 6.6l2.2-2.2a1 1 0 0 1 1-.25 11.4 11.4 0 0 0 3.6.57 1 1 0 0 1 1 1V20a1 1 0 0 1-1 1A17 17 0 0 1 3 4a1 1 0 0 1 1-1h3.5a1 1 0 0 1 1 1c0 1.25.2 2.45.57 3.57a1 1 0 0 1-.25 1z"/></svg>
  (604) 213 7780
</div>
<div class="abs topbar-links">
  <a>Register</a><span class="sep">|</span><a>Login</a><span class="sep">|</span><a>Wishlist</a><span class="sep">|</span><a>My Cart</a>
  <svg width="20" height="18" viewBox="0 0 20 18" aria-hidden="true"><path d="M3 6h14l-1.5 11h-11z" fill="#333"/><path d="M6.5 6V4a3.5 3.5 0 0 1 7 0v2" fill="none" stroke="#333" stroke-width="1.6"/></svg>
</div>

<!-- header -->
<div class="abs header"></div>
<div class="abs brand"><span class="brand-dot"></span><span class="brand-name">Tolmek</span></div>
<nav class="abs nav">
  <a class="active">Home</a><a>About Us</a><a>Products</a><a>Shop Now</a><a>Blogs</a><a>Contact</a>
</nav>

<!-- hero -->
<div class="abs hero" role="img" aria-label="Wide blue sky with fast-moving white clouds above a distant mountain range"></div>
<div class="abs play">
  <svg class="abs" style="left:33px;top:26px" width="28" height="34" viewBox="0 0 28 34" aria-hidden="true"><path d="M3 2l22 15L3 32z" fill="none" stroke="#fff" stroke-width="4" stroke-linejoin="round"/></svg>
</div>
<h1 class="abs hero-title">Care Home and Nail Bar Industry</h1>
<p class="abs hero-sub">Class aptent taciti sociosqu litora torquent</p>

<!-- welcome -->
<h2 class="abs welcome-title">Welcome to Tolmek</h2>
<div class="abs welcome-text">
  <p>Pellentesque faucibus Ut accumsan ultricies elit Maecenas at justo id velit placerat molestie Donec dictum lectus non odio</p>
  <p>Cras a ante vitae enim iaculis aliquam Mauris nunc quam venenatis nec euismod sit amet egestas placerat est Pellentesque habitant morbi tristique senectus et netus et malesuada fames ac turpis</p>
</div>
<a class="abs btn-more">READ MORE</a>
<div class="abs welcome-photo" role="img" aria-label="Close-up of manicured hands with red floral nail art"></div>

<!-- why choose us -->
<div class="abs why"></div>
<div class="abs why-photo" role="img" aria-label="Pedicured feet resting beside white orchid flowers"></div>
<h2 class="abs why-title">Why Choose Us for<br>Your Nail Care</h2>
<p class="abs why-text">Donec dictum lectus non odio Cras a ante vitae enim iaculis aliquam Mauris nunc quam venenatis nec euismod sit amet</p>
<div class="abs feature" style="left:601px;top:1352px"><h4>Hight Quality Product</h4><p>Morbi ornare gravida elit Integer</p></div>
<div class="abs feature" style="left:869px;top:1352px"><h4>Nail Experts</h4><p>Morbi ornare gravida elit Integer</p></div>
<div class="abs feature" style="left:601px;top:1439px"><h4>Luxury Feel</h4><p>Morbi ornare gravida elit Integer</p></div>
<div class="abs feature" style="left:869px;top:1439px"><h4>Treatment &amp; Care</h4><p>Morbi ornare gravida elit Integer</p></div>

<!-- products -->
<div class="abs products" role="img" aria-label="Soft backdrop of nail tools, polish bottles and dried flowers"></div>
<h2 class="abs section-title products-title">Our Products</h2>
<svg class="abs" style="left:84px;top:1832px" width="18" height="32" viewBox="0 0 18 32" aria-hidden="true"><path d="M15 2L3 16l12 14" fill="none" stroke="#999" stroke-width="3"/></svg>
<svg class="abs" style="left:1082px;top:1832px" width="18" height="32" viewBox="0 0 18 32" aria-hidden="true"><path d="M3 2l12 14L3 30" fill="none" stroke="#999" stroke-width="3"/></svg>

<div class="abs product-card" style="left:117px">
  <div class="product-img" role="img" aria-label="Two nail polish bottles, nude and black"></div>
  <div class="product-name">Product Name</div>
  <div class="product-desc">Morbi ornare gravida elit Integer</div>
  <div class="product-bar"><span class="price">$12.99</span><span class="buy">Buy Now</span></div>
</div>
<div class="abs product-card" style="left:360px">
  <div class="product-img" role="img" aria-label="Red nail polish bottle"></div>
  <div class="product-name">Product Name</div>
  <div class="product-desc">Morbi ornare gravida elit Integer</div>
  <div class="product-bar"><span class="price">$12.99</span><span class="buy">Buy Now</span></div>
</div>
<div class="abs product-card" style="left:603px">
  <div class="product-img" role="img" aria-label="Steel cuticle pusher tools"></div>
  <div class="product-name">Product Name</div>
  <div class="product-desc">Morbi ornare gravida elit Integer</div>
  <div class="product-bar"><span class="price">$12.99</span><span class="buy">Buy Now</span></div>
</div>
<div class="abs product-card" style="left:846px">
  <div class="product-img" role="img" aria-label="Amber cuticle oil dropper bottle"></div>
  <div class="product-name">Product Name</div>
  <div class="product-desc">Morbi ornare gravida elit Integer</div>
  <div class="product-bar"><span class="price">$12.99</span><span class="buy">Buy Now</span></div>
</div>

<!-- testimonials -->
<div class="abs testimonials"></div>
<svg class="abs" style="left:0;top:2440px" width="1200" height="130" viewBox="0 0 1200 130" preserveAspectRatio="none" aria-hidden="true">
  <path d="M0 100 C 300 150, 700 130, 1200 20 L1200 130 L0 130 Z" fill="#ffffff"/>
</svg>
<h2 class="abs test-title">Testimonials</h2>
<svg class="abs" style="left:104px;top:2294px" width="16" height="30" viewBox="0 0 16 30" aria-hidden="true"><path d="M14 2L3 15l11 13" fill="none" stroke="#fff" stroke-width="4"/></svg>
<svg class="abs" style="left:1063px;top:2294px" width="16" height="30" viewBox="0 0 16 30" aria-hidden="true"><path d="M2 2l11 13L2 28" fill="none" stroke="#fff" stroke-width="4"/></svg>

<div class="abs quote-card" style="left:207px">
  <p class="quote-text">Morbi diam mauris viverra in gravida eu mattis in ante Morbi eget arcu Morbi porta libero id ullamcorper nonummy nibh ligula pulvinar metus eget</p>
  <p class="quote-author">By Author Name</p>
</div>
<div class="abs avatar" style="left:172px" role="img" aria-label="Client portrait"></div>
<div class="abs quote-card" style="left:629px">
  <p class="quote-text">Morbi diam mauris viverra in gravida eu mattis in ante Morbi eget arcu Morbi porta libero id ullamcorper nonummy nibh ligula pulvinar metus eget</p>
  <p class="quote-author">By Author Name</p>
</div>
<div class="abs avatar" style="left:594px" role="img" aria-label="Client portrait"></div>

<!-- blog -->
<h2 class="abs section-title blog-title">Latest Blog</h2>
<div class="abs blog-card" style="left:113px">
  <div class="blog-img" role="img" aria-label="Hands receiving a manicure with flowers"></div>
  <div class="blog-date"><b>01</b><span>MAR</span></div>
  <div class="blog-head">Blog Tittle here</div>
  <p class="blog-text">sociosqu ad litora torquent per conubia nostra per inceptos hymenaeos</p>
  <a class="blog-more">READ MORE</a>
</div>
<div class="abs blog-card" style="left:441px">
  <div class="blog-img" role="img" aria-label="Nail technician filing a client's nails"></div>
  <div class="blog-date"><b>01</b><span>MAR</span></div>
  <div class="blog-head">Blog Tittle here</div>
  <p class="blog-text">sociosqu ad litora torquent per conubia nostra per inceptos hymenaeos</p>
  <a class="blog-more">READ MORE</a>
</div>
<div class="abs blog-card" style="left:769px">
  <div class="blog-img" role="img" aria-label="Manicure treatment at a nail bar"></div>
  <div class="blog-date"><b>01</b><span>MAR</span></div>
  <div class="blog-head">Blog Tittle here</div>
  <p class="blog-text">sociosqu ad litora torquent per conubia nostra per inceptos hymenaeos</p>
  <a class="blog-more">READ MORE</a>
</div>

<!-- footer -->
<svg class="abs footer-wave" viewBox="0 0 1200 513" preserveAspectRatio="none" aria-hidden="true">
  <defs>
    <linearGradient id="footerFill" x1="0" y1="0" x2="0" y2="1">
      <stop offset="0" stop-color="#1aa6e4"/>
      <stop offset="1" stop-color="#1566c8"/>
    </linearGradient>
  </defs>
  <path d="M0 60 C 400 20, 800 30, 1200 0 L1200 513 L0 513 Z" fill="url(#footerFill)"/>
</svg>

<div class="abs footer-col" style="left:155px">
  <h5>COMPANY</h5>
  <ul><li>Home</li><li>About Us</li><li>Nail Care</li><li>Our Products</li></ul>
</div>
<div class="abs social"><i></i><i></i><i></i><i></i></div>
<div class="abs footer-col" style="left:340px">
  <h5>RESOURCES</h5>
  <ul><li>Support</li><li>Testimonials</li><li>From Our Blogs</li><li>Contact Us</li></ul>
</div>
<div class="abs footer-col" style="left:566px">
  <h5>MY ACCOUNT</h5>
  <ul><li>My Cart</li><li>Checkout</li><li>Register</li><li>Log In</li></ul>
</div>
<div class="abs footer-col" style="left:829px;width:260px">
  <h5>CONTACT US</h5>
  <div class="contact-item">
    <svg width="14" height="18" viewBox="0 0 14 18" aria-hidden="true"><path d="M7 0a7 7 0 0 1 7 7c0 5-7 11-7 11S0 12 0 7a7 7 0 0 1 7-7z" fill="#fff"/><circle cx="7" cy="7" r="2.6" fill="#1a8bd8"/></svg>
    <span>Level 4, Marlow House 21-25 Penrose Road Ashfield NSW 2131</span>
  </div>
  <div class="contact-item">
    <svg width="14" height="14" viewBox="0 0 24 24" aria-hidden="true"><path fill="#fff" d="M6.6 10.8a15.1 15.1 0 0 0 6.6 6.6l2.2-2.2a1 1 0 0 1 1-.25 11.4 11.4 0 0 0 3.6.57 1 1 0 0 1 1 1V20a1 1 0 0 1-1 1A17 17 0 0 1 3 4a1 1 0 0 1 1-1h3.5a1 1 0 0 1 1 1c0 1.25.2 2.45.57 3.57a1 1 0 0 1-.25 1z"/></svg>
    <span>(02) 8841-3026</span>
  </div>
  <div class="contact-item">
    <svg width="14" height="14" viewBox="0 0 14 14" aria-hidden="true"><rect x="1" y="1" width="12" height="12" rx="1.5" fill="#fff"/><rect x="4" y="3" width="6" height="3" fill="#1a8bd8"/></svg>
    <span>+61 455 927 104</span>
  </div>
  <div class="contact-item">
    <svg width="14" height="12" viewBox="0 0 14 12" aria-hidden="true"><rect x="0" y="1" width="14" height="10" rx="1" fill="#fff"/><path d="M0 2l7 5 7-5" fill="none" stroke="#1a8bd8" stroke-width="1.4"/></svg>
    <span>hello@tolmekcare.com</span>
  </div>
</div>
<div class="abs payments"><i></i><i></i><i></i><i></i><i></i></div>

<div class="abs footer-rule"></div>
<p class="abs copyright">© 2017 Company Name All right reserved &nbsp;Term of Use</p>

</body>
</html>
```